Relocation/furniture installation company needs new business cards

we are a relocation and furniture installation company mainly dealing with corporate clients and we are looking for new business card ideas. Cards should incorporate our logo and list our website, phone number and services. The company is only 2 years old but with more staff joining we are in the need for more business cards, so something with an awesome design that is eye catching would go a long way to insure we get our name out there and look good to potential new clients.

Target Market(s)

Corporate

Industry/Entity Type

Trade

Contact Information for Business Card

www.mervoline.co.nz
0508 4 bravok

furniture installation
business relocations
joinery installation
commercial property maintenance

Colors
0592cd
34a7d8
85cae6
85acd3
0356a4
cfdfed
cee9f5
757575
474747

Requirements
Must have
• Business relocations and furniture installation specialists
Nice to have
• something that incorporates our logo.

```html
<!DOCTYPE html>
<html lang="en">
<head>
<meta charset="utf-8">
<title>Mervoline business cards</title>
<link href="https://fonts.googleapis.com/css2?family=Montserrat:wght@500;600&family=Open+Sans:wght@400&display=swap" rel="stylesheet">
<style>
  :root {
    --backdrop: #1c1c1c;
    --brand-blue: #283b9a;
    --brand-blue-dark: #1f2f85;
    --sky: #34a7d8;
    --sky-light: #85cae6;
    --ink-grey: #474747;
    --soft-grey: #757575;
    --white: #ffffff;
  }
  * { box-sizing: border-box; margin: 0; padding: 0; }
  html, body { width: 1200px; height: 852px; overflow: hidden; }
  body {
    background: var(--backdrop);
    position: relative;
    font-family: "Open Sans", Arial, sans-serif;
  }
  .card {
    position: absolute;
    width: 620px;
    height: 354px;
    border-radius: 22px;
    overflow: hidden;
  }
  .card-front {
    left: 90px;
    top: 40px;
    background: var(--brand-blue);
    display: flex;
    align-items: center;
    justify-content: center;
  }
  .wordmark {
    font-family: "Montserrat", Arial, sans-serif;
    font-weight: 600;
    letter-spacing: 4px;
    display: flex;
    align-items: center;
    gap: 14px;
  }
  .card-front .wordmark { color: var(--white); font-size: 44px; }
  .wordmark-square {
    display: block;
    width: 26px;
    height: 26px;
    background: var(--sky);
  }
  .card-back {
    left: 490px;
    top: 458px;
    background: var(--white);
  }
  .card-back .wordmark {
    position: absolute;
    right: 38px;
    top: 48px;
    color: var(--brand-blue);
    font-size: 28px;
    gap: 10px;
  }
  .card-back .wordmark-square { width: 18px; height: 18px; }
  .band { position: absolute; left: 0; top: 0; }
  .building-art {
    position: absolute;
    right: 22px;
    top: 126px;
    width: 200px;
    height: 128px;
    background: linear-gradient(135deg, var(--sky-light), var(--sky) 55%, #0356a4);
    border: 3px solid var(--brand-blue);
  }
  .identity {
    position: absolute;
    left: 38px;
    top: 98px;
  }
  .person-name {
    font-family: "Montserrat", Arial, sans-serif;
    font-weight: 600;
    font-size: 26px;
    line-height: 32px;
    color: var(--brand-blue);
    letter-spacing: 1px;
  }
  .person-role {
    font-size: 14px;
    line-height: 19px;
    color: var(--ink-grey);
    margin-bottom: 4px;
  }
  .services { list-style: none; }
  .services li {
    font-size: 14.5px;
    color: var(--ink-grey);
    line-height: 19px;
  }
  .contacts {
    position: absolute;
    left: 38px;
    top: 256px;
    list-style: none;
    color: var(--white);
  }
  .contacts li {
    font-size: 14.5px;
    line-height: 20px;
    display: flex;
    align-items: center;
    gap: 10px;
  }
  .contacts svg { width: 11px; height: 11px; flex: none; }
  .contacts .no-icon { padding-left: 21px; }
</style>
</head>
<body>
  <section class="card card-front">
    <div class="wordmark"><span class="wordmark-square"></span>MERVOLINE</div>
  </section>

  <section class="card card-back">
    <svg class="band" width="620" height="354" viewBox="0 0 620 354" aria-hidden="true">
      <polygon points="0,246 370,246 370,226 400,226 400,150 430,150 430,120 620,120 620,354 0,354" fill="var(--brand-blue)"/>
    </svg>
    <div class="building-art" role="img" aria-label="Illustration of glass office buildings in blue tones"></div>

    <div class="wordmark"><span class="wordmark-square"></span>MERVOLINE</div>

    <div class="identity">
      <p class="person-name">ROWAN TALLIS</p>
      <p class="person-role">Director</p>
      <ul class="services">
        <li>furniture installation</li>
        <li>business relocations</li>
        <li>joinery installation</li>
        <li>commercial property maintenance</li>
      </ul>
    </div>

    <ul class="contacts">
      <li>
        <svg viewBox="0 0 12 12"><path d="M2.5 1 L4.5 1 L5 3.5 L3.8 4.5 Q5 7 7.5 8.2 L8.5 7 L11 7.5 L11 9.5 Q11 11 9.5 11 Q1 10.5 1 2.5 Q1 1 2.5 1 Z" fill="var(--white)"/></svg>
        +330 5184 2093
      </li>
      <li>
        <svg viewBox="0 0 12 12"><rect x="0.8" y="2.5" width="10.4" height="7" fill="none" stroke="var(--white)" stroke-width="1.3"/><path d="M1 3 L6 7 L11 3" fill="none" stroke="var(--white)" stroke-width="1.3"/></svg>
        info@mervoline.co.nz
      </li>
      <li>
        <svg viewBox="0 0 12 12"><circle cx="6" cy="6" r="5" fill="none" stroke="var(--white)" stroke-width="1.2"/><path d="M1 6 H11 M6 1 Q3 6 6 11 Q9 6 6 1" fill="none" stroke="var(--white)" stroke-width="1"/></svg>
        www.mervoline.co.nz
      </li>
      <li class="no-icon">0508 4 bravok</li>
    </ul>
  </section>
</body>
</html>
```